Design Contest: A New Look & Feel for VORMI.nl

🌍 Context
VORMI.nl combines knowledge about supplements, ingredients, and spirituality, while also offering lectures, retreats, and training programs.
We are not a foundation or donation platform, but an open knowledge network with a professional, warm, and trustworthy presence.

Our mission is to connect science and soul, sharing valuable insights and experiences that inspire both rational understanding and spiritual growth.

🎯 The Goal
We’re inviting talented web designers and visual creatives to redesign VORMI.nl into a modern, elegant, and emotionally resonant platform.

The new design should communicate:
Warmth and human connection,
Professionalism and clarity, and
A sense of discovery and inspiration.
The site will serve as a central hub for education, community, and conscious travel β€” bridging science, nature, and spirituality.

Landing Page (One-Pager):

A welcoming introduction to VORMI that immediately conveys our essence: knowledge, connection, and inspiration.
Visually guides visitors toward our main areas β€” journeys, education, and knowledge β€” with clear calls to action.

Travel Page Design:

A dedicated layout for a spiritual journey or retreat
Should evoke curiosity, emotion, and trust β€” encouraging visitors to read the program and feel inspired to book.

Education Page Design:
A page for one specific training or lecture.
Should look professional and engaging, highlighting benefits and making visitors eager to sign up.

Ingredient Page Design:
A clean, structured layout for an ingredient (e.g., Velotrin K7 Matrix®).
Should balance science and accessibility β€” informative yet visually appealing, showing related insights or products.

✨ What We’re Looking For
🌸 Warm, Friendly Aesthetic
A soft, grounded color palette (see moodboard below).
A look that feels welcoming, safe, modern, and inspiring.
Avoid harsh contrasts or corporate coldness β€” aim for organic elegance and heart-centered design.

🌿 Clean, Airy Layout
Generous white/cream space for readability and calm.
Rounded corners, smooth transitions, and balanced composition.
Use light textures (paper, waves, or organic shapes) to evoke warmth.

✍️ Modern Typography
Body text: Nunito, Lato, or Raleway β€” friendly, clear, and easy to read.
Headings: Playfair Display or Quicksand β€” elegant and expressive.
Typography should reflect both expertise and approachability.

πŸ”— Clear Navigation
Logical, intuitive structure with the following key areas:
Knowledge Hub – Products – Activities – About – Contact
Clear, soft-toned buttons and navigation encouraging exploration.
Consider β€œrelated content” cards or visual pathways connecting knowledge, events, and products.

πŸ’« Visual Integration
Create visual links between knowledge, activities, and products (e.g., tags, badges, or modular cards).
Filters or category highlights to navigate supplement/ingredient content easily.
Visual flow should feel alive yet harmonious.

🧠 Local & Human Connection
Photography that emphasizes real people, learning moments, and connection with nature.
Avoid clinical or corporate stock images β€” show authenticity, empathy, and light.

🀝 Community Features
Dedicated space for reviews, expert Q&A, or interaction.
These areas should radiate trust, safety, and a sense of belonging.

🧩 Brisk CMS Compatibility
Must be responsive and easily built within Brisk CMS (drag-and-drop).
Show where dynamic content (articles, events, or journeys) will be placed and how cards adapt to different devices.

🎨 Moodboard & Color Palette
Color Name HEX Code Emotion & Use
Warm Beige #DFBAAA The grounding base color β€” evokes natural warmth, balance, and calm. Ideal for backgrounds and section dividers.
Light Cream #F5EAE5 Airy and gentle β€” conveys purity, openness, and readability. Use for backgrounds and whitespace.
Deep Aubergine #431624 Adds depth and mystery β€” perfect for headlines, highlights, or footers. Symbolizes introspection and wisdom.
Wine Red #750E2B Expresses vitality, heart energy, and focus. Ideal for buttons, accents, or key highlights.
Burnt Orange #F26C2E Brings creative spark and positivity. Great for hover states, subtle icons, or energetic accents.
Mustard Yellow #B68620 Symbolizes light, optimism, and knowledge. Use as a secondary accent or highlight.

Color philosophy:
This palette represents the meeting point between Earth and Fire β€” grounding warmth combined with vibrant inspiration.
It visually communicates the essence of VORMI: trustworthy science, human connection, and transformative energy.

🧠 Target Audience
Health professionals and therapists seeking supplement and ingredient education.
Consumers and conscious individuals interested in wellbeing, spirituality, and science.
Spiritual explorers looking for transformative journeys and community learning.

πŸ’‘ Functional & Structural Goals
The site should clearly showcase VORMI’s four pillars:
Journeys & Retreats – spiritual travel experiences.
Academy & Trainings – professional education and lectures.
Knowledge Center – accessible supplement & ingredient knowledge (scientific yet warm).

πŸ“¦ What to Submit
A homepage concept (desktop + mobile).
Final delivery as a layererd PSD

```html
<!DOCTYPE html>
<html lang="en">
<head>
<meta charset="utf-8">
<title>VORMI – Connecting Science, Soul, and Human Wellbeing</title>
<link rel="stylesheet" href="https://fonts.googleapis.com/css2?family=Fraunces:wght@400;500&family=Lato:wght@400;700&display=swap">
<style>
:root{
  --sky:#4FB0E0;
  --sky-soft:#EEF6FC;
  --crimson:#D90D55;
  --blush:#FEF2F5;
  --blush-deep:#FCE8EE;
  --arc:#E3F1FA;
  --navy:#133F5E;
  --ink:#222;
  --muted:#7A8591;
  --white:#fff;
  --star:#F5B82E;
}
*{margin:0;padding:0;box-sizing:border-box}
html,body{width:1200px;height:4318px;overflow:hidden}
body{font-family:'Lato',sans-serif;color:var(--ink);background:var(--white);position:relative}
.abs{position:absolute}
.brand{display:flex;align-items:center;gap:12px;font-weight:700;color:var(--crimson);letter-spacing:.5px;line-height:1}
.brand .dot{width:36px;height:36px;border-radius:50%;background:var(--crimson)}
.brand span{font-size:26px}

/* nav */
.site-nav{top:0;left:0;width:1200px;height:102px;background:var(--white)}
.site-nav .brand{position:absolute;left:100px;top:32px}
.nav-links a{position:absolute;top:37px;color:var(--ink);text-decoration:none;font-size:14px}
.nav-links a.active{color:var(--sky)}
.nav-indicator{position:absolute;left:557px;top:99px;width:64px;height:3px;background:var(--sky)}
.contact-btn{position:absolute;left:975px;top:27px;width:125px;height:36px;border:1.5px solid #ddd;border-radius:18px;color:var(--crimson);font-size:12px;font-weight:700;display:flex;align-items:center;justify-content:center}

/* hero */
.hero{top:102px;left:0;width:1200px;height:601px;background:linear-gradient(180deg,#55B4E3,#4FABD9)}
.hero-photo{position:absolute;right:0;top:0;width:640px;height:601px;background:radial-gradient(ellipse at 60% 55%,#E9B79E 0%,#C98B6E 22%,rgba(79,176,224,0) 55%)}
.hero h1{position:absolute;left:103px;top:68px;font-family:'Fraunces',serif;font-weight:400;font-size:58px;line-height:66px;color:var(--white)}
.hero p{position:absolute;left:101px;top:296px;width:330px;font-size:15px;line-height:24px;color:var(--white)}
.btn-pill{display:flex;align-items:center;justify-content:space-between;border-radius:24px;font-weight:700}
.hero .start{position:absolute;left:101px;top:445px;width:173px;height:46px;background:var(--white);color:var(--navy);font-size:15px;padding:0 5px 0 27px}
.arrow-dot{width:36px;height:36px;border-radius:50%;background:var(--navy);display:flex;align-items:center;justify-content:center}
.hero .how{position:absolute;left:295px;top:459px;color:var(--white);font-size:14px;font-weight:700;text-decoration:underline}
.video-thumb{position:absolute;left:912px;top:368px;width:164px;height:164px;border-radius:50%;border:6px solid rgba(255,255,255,.35);background:radial-gradient(circle at 50% 60%,#F3D7C8,#2E8B6E)}
.play{position:absolute;left:56px;top:56px;width:40px;height:40px;border-radius:50%;background:var(--crimson);display:flex;align-items:center;justify-content:center}

/* stats */
.stats{top:703px;left:0;width:1200px;height:155px;background:var(--crimson);color:var(--white)}
.stat{position:absolute;top:33px}
.stat b{display:block;font-family:'Fraunces',serif;font-weight:400;font-size:26px}
.stat span{display:block;font-size:15px;line-height:22px;margin-top:6px}
.stat-rule{position:absolute;top:28px;width:1px;height:92px;background:rgba(255,255,255,.6)}
.explore-btn{position:absolute;left:952px;top:57px;width:139px;height:42px;background:var(--white);color:var(--crimson);border-radius:21px;font-size:12px;font-weight:700;display:flex;align-items:center;justify-content:center}

/* shared */
.eyebrow{font-size:12px;color:var(--crimson)}
.sec-title{font-weight:700;font-size:36px;line-height:44px;color:var(--navy);letter-spacing:-.5px}
.lede{font-size:15px;line-height:24px;color:var(--ink)}
.cta{background:var(--crimson);color:var(--white);border-radius:22px;font-size:12px;font-weight:700;display:flex;align-items:center;justify-content:center}

/* pillars */
.pillars{top:858px;left:0;width:1200px;height:644px;overflow:hidden}
.pillars .eyebrow{position:absolute;top:85px;width:1200px;text-align:center}
.pillars .sec-title{position:absolute;top:110px;width:1200px;text-align:center}
.pillar h3{font-weight:400;font-size:26px;color:var(--sky);margin-bottom:14px}
.pillar p{font-size:14.5px;line-height:24px}
.icon-ring{position:absolute;width:104px;height:104px;border-radius:50%;background:var(--sky-soft);display:flex;align-items:center;justify-content:center}

.who{top:1502px;left:0;width:1200px;height:360px;background:var(--blush)}
.journeys{top:1862px;left:0;width:1200px;height:860px}
.tile{position:absolute}

/* offer */
.offer{top:2722px;left:0;width:1200px;height:703px;background:var(--sky-soft)}
.card{position:absolute;top:255px;width:316px;height:313px;background:var(--white);border-radius:14px;padding:20px 23px}
.card .ico{width:78px;height:78px;border-radius:8px;background:var(--sky);display:flex;align-items:center;justify-content:center;margin-bottom:16px}
.card h3{font-size:26px;font-weight:700;color:var(--navy);letter-spacing:-.5px;margin-bottom:12px}
.card p{font-size:14px;line-height:21.5px;width:262px}

/* testimonials */
.voices{top:3425px;left:0;width:1200px;height:573px}
.person{position:absolute;top:232px;width:316px;text-align:center}
.avatar{width:78px;height:78px;border-radius:50%;margin:0 auto 12px}
.person h4{font-size:18px;font-weight:400;color:var(--navy)}
.person small{display:block;font-size:10px;color:var(--muted);margin-top:4px}
.quote{margin-top:24px;background:var(--sky-soft);height:123px;padding:18px 18px 0;text-align:left;font-size:13px;line-height:22px}
.stars{text-align:center;color:var(--star);font-size:17px;letter-spacing:4px;margin-top:2px}

/* footer */
.site-foot{top:3998px;left:0;width:1200px;height:320px;background:var(--sky);color:var(--white)}
.site-foot .brand{position:absolute;left:105px;top:62px;color:var(--white)}
.site-foot .brand .dot{background:var(--white)}
.site-foot .brand span{font-size:32px}
.social{position:absolute;top:192px;left:110px;display:flex;gap:27px}
.social i{display:block;width:24px;height:24px;border-radius:50%;background:var(--white)}
.foot-col{position:absolute;top:58px}
.foot-col h5{font-size:19px;font-weight:400;margin-bottom:18px;color:#EAF6FD}
.foot-col a{display:block;color:var(--white);text-decoration:none;font-size:15px;margin-bottom:14px}
.foot-rule{position:absolute;left:100px;top:278px;width:1000px;height:1px;background:rgba(255,255,255,.4)}
.copy{position:absolute;top:291px;width:1200px;text-align:center;font-size:11px}
</style>
</head>
<body>

<header class="site-nav abs">
  <div class="brand"><i class="dot"></i><span>VORMI</span></div>
  <nav class="nav-links">
    <a class="active" href="#" style="left:441px">Welcome</a>
    <a href="#" style="left:544px">Workshops</a>
    <a href="#" style="left:665px">Courses</a>
    <a href="#" style="left:763px">Agenda</a>
    <a href="#" style="left:857px">Travel</a>
  </nav>
  <div class="nav-indicator"></div>
  <div class="contact-btn">CONTACT US</div>
</header>

<section class="hero abs">
  <div class="hero-photo" role="img" aria-label="Joyful red-haired woman in a floral blouse making peace signs against a soft blue flower field"></div>
  <h1>Connecting Science,<br>Soul, and Human<br>Wellbeing</h1>
  <p>A warm knowledge network where research,<br>experience, and conscious living meet.<br>Discover journeys, education, and insights<br>designed to support a healthier, more<br>connected life.</p>
  <div class="start btn-pill">Get Started
    <span class="arrow-dot"><svg width="16" height="16" viewBox="0 0 16 16" fill="none" stroke="#fff" stroke-width="1.8"><path d="M3 8h10M9 4l4 4-4 4"/></svg></span>
  </div>
  <a class="how">How It Works</a>
  <div class="video-thumb" role="img" aria-label="Video preview of a smiling woman outdoors">
    <div class="play"><svg width="14" height="16" viewBox="0 0 14 16"><path d="M2 1l11 7-11 7z" fill="#fff"/></svg></div>
  </div>
</section>

<section class="stats abs">
  <div class="stat" style="left:105px"><b>3,200+</b><span>Participants in<br>trainings and retreats</span></div>
  <div class="stat-rule" style="left:323px"></div>
  <div class="stat" style="left:370px"><b>150+</b><span>Scientific ingredient<br>insights and articles</span></div>
  <div class="stat-rule" style="left:588px"></div>
  <div class="stat" style="left:634px"><b>12Years+</b><span>Sharing knowledge<br>with heart and clarity</span></div>
  <div class="explore-btn">Explore VORMI</div>
</section>

<section class="pillars abs">
  <div class="eyebrow">Our Pillars</div>
  <h2 class="sec-title">Learn, Travel, and Explore With Us</h2>
  <svg class="abs" style="left:0;top:0" width="1200" height="644">
    <circle cx="600" cy="644" r="300" fill="none" stroke="var(--arc)" stroke-width="5"/>
    <circle cx="600" cy="644" r="218" fill="var(--blush-deep)"/>
  </svg>
  <div class="pillar abs" style="left:300px;top:200px;width:600px;text-align:center">
    <h3>Journeys &amp; Retreats</h3>
    <p>Travel with intention. Deepen your connection to<br>nature, community, and yourself.</p>
  </div>
  <div class="pillar abs" style="left:140px;top:330px;width:280px">
    <h3>Academy &amp; Trainings</h3>
    <p>Professional education rooted in<br>science and humanity, accessible to<br>all curious learners.</p>
  </div>
  <div class="pillar abs" style="left:820px;top:310px;width:260px">
    <h3>Knowledge Center</h3>
    <p>Ingredients and supplements<br>explained clearly. Science made<br>friendly, warm, and useful.</p>
  </div>
  <div class="icon-ring" style="left:548px;top:307px"><svg width="46" height="46" viewBox="0 0 46 46" fill="none" stroke="#4FB0E0" stroke-width="2.5"><circle cx="10" cy="12" r="5"/><circle cx="36" cy="34" r="5"/><path d="M15 12h18a6 6 0 010 12H13a6 6 0 000 12h18"/></svg></div>
  <div class="icon-ring" style="left:298px;top:447px"><svg width="48" height="48" viewBox="0 0 48 48" fill="none" stroke="#4FB0E0" stroke-width="2.5"><rect x="4" y="6" width="30" height="24" rx="2"/><path d="M10 14l8 8"/><circle cx="36" cy="30" r="5"/><path d="M28 46v-6a8 8 0 0116 0v6"/></svg></div>
  <div class="icon-ring" style="left:798px;top:447px"><svg width="48" height="48" viewBox="0 0 48 48" fill="none" stroke="#4FB0E0" stroke-width="2.5"><circle cx="14" cy="12" r="6"/><path d="M4 30a10 10 0 0120 0"/><path d="M28 8h14M28 15h14M28 22h10"/><circle cx="34" cy="34" r="5"/><path d="M24 46a10 10 0 0120 0"/></svg></div>
  <div class="brand abs" style="left:522px;top:540px"><i class="dot"></i><span style="font-size:30px">VORMI</span></div>
</section>

<section class="who abs">
  <div class="eyebrow abs" style="left:100px;top:92px">Who We Are</div>
  <h2 class="sec-title abs" style="left:100px;top:113px;width:520px">A Warm Network Connecting<br>Science and Soul</h2>
  <p class="lede abs" style="left:100px;top:224px;width:470px">VORMI is a place where knowledge feels human.<br>We combine trusted scientific research with personal</p>
  <p class="lede abs" style="left:676px;top:84px;width:440px">experience, spiritual awareness, and community learning.<br>Our mission is simple: make wellbeing understandable,<br>compassionate, and grounded in reality.<br>We are not a foundation, not a donation platform, and not<br>a closed circle of experts speaking only to themselves.</p>
  <div class="btn-pill abs" style="left:676px;top:232px;width:173px;height:46px;background:var(--crimson);color:#fff;font-size:15px;padding:0 5px 0 26px">Get Started
    <span class="arrow-dot" style="background:#fff"><svg width="16" height="16" viewBox="0 0 16 16" fill="none" stroke="#D90D55" stroke-width="1.8"><path d="M3 8h10M9 4l4 4-4 4"/></svg></span>
  </div>
</section>

<section class="journeys abs">
  <div class="eyebrow abs" style="left:100px;top:88px">Featured Journey</div>
  <h2 class="sec-title abs" style="left:100px;top:108px;width:420px">Journeys Designed for<br>Inner Connection</h2>
  <p class="lede abs" style="left:657px;top:101px;width:440px">Step away from noise and into nature.<br>Our retreats combine guidance, reflection, and safe<br>community spaces to help you reconnect with<br>yourself and the world around you.</p>
  <div class="tile" style="left:100px;top:288px;width:230px;height:370px;background:linear-gradient(160deg,#6B5A44,#2D2A25 55%,#8C8278)" role="img" aria-label="Cliffside monastery with golden roofs"></div>
  <div class="tile" style="left:357px;top:288px;width:230px;height:370px;background:linear-gradient(180deg,#9AA1A8,#C9B39B 35%,#8A6E8E 60%,#5A4660)" role="img" aria-label="Misty heather field at sunrise"></div>
  <div class="tile" style="left:613px;top:245px;width:230px;height:456px;background:linear-gradient(180deg,#34464F,#7A5A3C 40%,#5B5A58 75%,#3E4448)" role="img" aria-label="Large bronze Buddha statue above a temple">
    <svg class="abs" style="left:97px;top:208px" width="36" height="22" viewBox="0 0 36 22" fill="none" stroke="#fff" stroke-width="2.5"><path d="M2 11C8 3 28 3 34 11 28 19 8 19 2 11z"/><circle cx="18" cy="11" r="4" fill="#fff"/></svg>
  </div>
  <div class="tile" style="left:870px;top:288px;width:230px;height:370px;background:linear-gradient(180deg,#BFD9EA,#3C6E3A 35%,#5B8C3E 60%,#2FC6D6 80%,#57D6DF)" role="img" aria-label="Tropical mountain over turquoise lagoon with overwater bungalows"></div>
  <div class="cta abs" style="left:513px;top:748px;width:174px;height:42px">Discover the Journey</div>
</section>

<section class="offer abs">
  <div class="eyebrow abs" style="left:100px;top:93px">What We Offer</div>
  <h2 class="sec-title abs" style="left:100px;top:113px;width:420px">Professional Education<br>With Heart and Clarity</h2>
  <p class="lede abs" style="left:657px;top:121px;width:440px">Support that feels human, respectful, and grounded in<br>real knowledge.</p>
  <div class="card" style="left:100px">
    <div class="ico"><svg width="50" height="50" viewBox="0 0 50 50" fill="none" stroke="#fff" stroke-width="2.2"><circle cx="14" cy="10" r="5"/><circle cx="36" cy="10" r="5"/><path d="M6 44V24a8 8 0 0116 0v20M28 44V24a8 8 0 0116 0v20M16 30h18"/></svg></div>
    <h3>One-on-One Support</h3>
    <p>Work with compassionate, trained<br>experts in private sessions. Whether<br>you're struggling with difficult emotions,<br>stress, or anxiety, find clarity and<br>support in a safe space.</p>
  </div>
  <div class="card" style="left:443px">
    <div class="ico"><svg width="50" height="50" viewBox="0 0 50 50" fill="none" stroke="#fff" stroke-width="2.2"><circle cx="25" cy="14" r="5"/><circle cx="11" cy="20" r="4"/><circle cx="39" cy="20" r="4"/><path d="M16 36a9 9 0 0118 0M3 38a8 8 0 0114-4M47 38a8 8 0 00-14-4"/></svg></div>
    <h3>Group Support</h3>
    <p>Guided group conversations where<br>people share experiences, learn from<br>each other, and feel less alone.<br>Every session is led by a professional to<br>keep things supportive, structured, and<br>comforting.</p>
  </div>
  <div class="card" style="left:786px">
    <div class="ico"><svg width="50" height="50" viewBox="0 0 50 50" fill="none" stroke="#fff" stroke-width="2.2"><path d="M25 30l-9-9a5 5 0 017-7l2 2 2-2a5 5 0 017 7z"/><path d="M4 28l8 14h14M46 28l-8 14H24"/></svg></div>
    <h3>Self-Guided Tools</h3>
    <p>Helpful exercises and resources you can<br>use anytime.<br>Simple practices designed to bring<br>calm, emotional balance, and relief on<br>your own terms.</p>
  </div>
  <div class="cta abs" style="left:532px;top:610px;width:136px;height:40px">Discover More</div>
</section>

<section class="voices abs">
  <div class="eyebrow abs" style="top:80px;width:1200px;text-align:center">What We Offer</div>
  <h2 class="sec-title abs" style="top:102px;width:1200px;text-align:center">Professional Education With<br>Heart and Clarity</h2>
  <div class="person" style="left:98px">
    <div class="avatar" style="background:#5DA9D6" role="img" aria-label="Portrait of Jhon Doe"></div>
    <h4>Jhon Doe</h4><small>Company X</small>
    <div class="quote">I finally felt understood and truly seen. Talking with someone who cared helped me breathe and find myself again.<div class="stars">★★★★☆</div></div>
  </div>
  <div class="person" style="left:440px">
    <div class="avatar" style="background:#E8A397" role="img" aria-label="Portrait of Jean Doe"></div>
    <h4>Jean Doe</h4><small>Company X</small>
    <div class="quote">Just having someone to listen without judgment made a huge difference in how I see myself and the world.<div class="stars">★★★★☆</div></div>
  </div>
  <div class="person" style="left:783px">
    <div class="avatar" style="background:#7BC4E4" role="img" aria-label="Portrait of Jean Doe"></div>
    <h4>Jean Doe</h4><small>Company X</small>
    <div class="quote">I feel lighter, calmer, and more in control of my emotions and my life. I'm so grateful for the support.<div class="stars">★★★★☆</div></div>
  </div>
</section>

<footer class="site-foot abs">
  <div class="brand"><i class="dot"></i><span>VORMI</span></div>
  <div class="social"><i></i><i></i><i></i><i></i></div>
  <div class="foot-col" style="left:527px"><h5>Marketplace</h5><a>Explore</a><a>Travel</a><a>How it Works</a><a>Help</a></div>
  <div class="foot-col" style="left:758px"><h5>Resources</h5><a>About Us</a><a>Events</a><a>Tutorials</a><a>News Blog</a></div>
  <div class="foot-col" style="left:968px"><h5>Links</h5><a>Updates</a><a>Newsletter</a><a>Careers</a><a>Become a Partner</a></div>
  <div class="foot-rule"></div>
  <div class="copy">© Copyright 2025, All Rights Reserved</div>
</footer>

</body>
</html>
```